BrimFalcon Business Cards

We have a defined brand. Please visit our website to get a feel for the product and the color pallets. www.brimfalcon-demo.com

We need an updated, world class business card design. (See the attached existing card design). Please utilize BOTH sides of the card as shown and be creative with the layout. I do want the horse head icon to be positioned as it is with the existing card.

The remainder of the layout can be customized and I also want it vertically oriented.

Attached are the logo files and please use the colors as follows:
Green - #A5CE39
Tan - #CDBD99
Black

Feel free to play with the colors.

```html
<!DOCTYPE html>
<html lang="en">
<head>
<meta charset="utf-8">
<title>BrimFalcon Labs – Business Cards</title>
<link href="https://fonts.googleapis.com/css2?family=Michroma&family=Open+Sans:wght@400;600;700&display=swap" rel="stylesheet">
<style>
  :root {
    --bg: #1c1c1c;
    --white: #ffffff;
    --black: #0d0d0d;
    --green-light: #c8d22c;
    --green-mid: #8fbb3a;
    --green-deep: #3b9148;
    --text: #111111;
  }
  * { box-sizing: border-box; margin: 0; padding: 0; }
  html, body { width: 1200px; height: 976px; overflow: hidden; }
  body {
    background: var(--bg);
    position: relative;
    font-family: "Open Sans", Arial, sans-serif;
    color: var(--text);
  }
  .card {
    position: absolute;
    width: 600px;
    height: 343px;
    overflow: hidden;
    box-shadow: 0 10px 30px rgba(0,0,0,0.55);
  }
  /* Front */
  .card-front {
    left: 50px;
    top: 150px;
    background: var(--white);
  }
  .brand {
    position: absolute;
    left: 118px;
    top: 118px;
    display: flex;
    align-items: center;
    gap: 16px;
  }
  .brand-dot {
    width: 58px;
    height: 58px;
    border-radius: 50%;
    background: var(--black);
    flex: none;
  }
  .brand-name {
    font-weight: 700;
    font-size: 40px;
    line-height: 1;
    color: var(--black);
    letter-spacing: 0.5px;
  }
  .brand-tagline {
    font-weight: 600;
    font-size: 15px;
    letter-spacing: 6px;
    color: var(--black);
    margin-top: 8px;
  }
  /* Back */
  .card-back {
    left: 550px;
    top: 520px;
    background: radial-gradient(circle at 52% 60%, var(--green-light) 0%, var(--green-mid) 35%, var(--green-deep) 80%);
  }
  .back-arc {
    position: absolute;
    right: -150px;
    top: -190px;
    width: 470px;
    height: 470px;
    border-radius: 50%;
    background: var(--white);
    border: 9px solid var(--black);
  }
  .back-mark {
    position: absolute;
    right: 70px;
    top: 70px;
    width: 112px;
    height: 112px;
    border-radius: 50%;
    background: var(--black);
  }
  .person {
    position: absolute;
    left: 56px;
    top: 82px;
  }
  .person-name {
    font-family: "Michroma", "Open Sans", sans-serif;
    font-size: 17px;
    letter-spacing: 4px;
    color: var(--black);
  }
  .person-role {
    font-size: 10px;
    margin-top: 2px;
    color: var(--black);
  }
  .contacts {
    position: absolute;
    left: 56px;
    top: 170px;
    list-style: none;
  }
  .contacts li {
    display: flex;
    align-items: flex-start;
    gap: 10px;
    font-size: 13px;
    line-height: 1.3;
    margin-bottom: 7px;
    color: var(--black);
  }
  .contacts svg { width: 16px; height: 16px; flex: none; margin-top: 1px; }
</style>
</head>
<body>

<section class="card card-front" aria-label="Card front">
  <div class="brand">
    <span class="brand-dot"></span>
    <div>
      <div class="brand-name">BrimFalcon Labs</div>
      <div class="brand-tagline">Performance Driven EVs</div>
    </div>
  </div>
</section>

<section class="card card-back" aria-label="Card back">
  <div class="back-arc"></div>
  <span class="back-mark"></span>

  <div class="person">
    <div class="person-name">MARCUS VALE</div>
    <div class="person-role">CEO/Managing Director</div>
  </div>

  <ul class="contacts">
    <li>
      <svg viewBox="0 0 24 24"><path fill="#0d0d0d" d="M6.6 10.8a15 15 0 0 0 6.6 6.6l2.2-2.2a1 1 0 0 1 1-.25 11.4 11.4 0 0 0 3.6.57 1 1 0 0 1 1 1V20a1 1 0 0 1-1 1A17 17 0 0 1 3 4a1 1 0 0 1 1-1h3.5a1 1 0 0 1 1 1c0 1.25.2 2.45.57 3.6a1 1 0 0 1-.25 1z"/></svg>
      <span>555-014-7720</span>
    </li>
    <li>
      <svg viewBox="0 0 24 24"><path fill="#0d0d0d" d="M7 3h10v5H7zM4 9h16a2 2 0 0 1 2 2v6h-4v4H6v-4H2v-6a2 2 0 0 1 2-2zm4 7v3h8v-3z"/></svg>
      <span>555-014-7720</span>
    </li>
    <li>
      <svg viewBox="0 0 24 24"><path fill="#0d0d0d" d="M2 5h20v14H2zm2 2v.5l8 5 8-5V7zm0 2.8V17h16V9.8l-8 5z"/></svg>
      <span>mvale@brimfalcon-demo.com</span>
    </li>
    <li>
      <svg viewBox="0 0 24 24" fill="none" stroke="#0d0d0d" stroke-width="1.6"><circle cx="12" cy="12" r="9"/><ellipse cx="12" cy="12" rx="4" ry="9"/><path d="M3 12h18M5 7h14M5 17h14"/></svg>
      <span>www.brimfalcon-demo.com</span>
    </li>
    <li>
      <svg viewBox="0 0 24 24"><path fill="#0d0d0d" d="M12 2a7 7 0 0 1 7 7c0 5-7 13-7 13S5 14 5 9a7 7 0 0 1 7-7zm0 4a3 3 0 1 0 0 6 3 3 0 0 0 0-6z"/></svg>
      <span>418 Orchard Lane NW<br>Suite 210, Fairmont MI 49000</span>
    </li>
  </ul>
</section>

</body>
</html>
```